Marigold Cleaning Service LTD its all about cleaning ( Domestic Cleaning, Commercial Cleaning, Student Accommodations, Corridors, Halls & Common Areas). I'm looking for POSH/ ELEGANT LOOKING design of flyers, which presents all Services we provide, it also should include 5% discount for new customers, contact details: website: www.marigold-clean.example.co.uk email address: marigoldservice@mailbox-example.com Mobile phone no: 07700900417 and home no: 01632960582 . I would like to include logo of the company, without any pictures of buckets etc.(that in my opinion pictures like that looks "cheap"). It should be design which perfectly match logo of the company, I would like also to include slogan of Marigold "You Deserve Marigold Cleaners". I was thinking to make those flyers, bright "clean" (maybe background could be beige color, on the other hand I think Navy color looks elegant as well, I'm looking for something posh NOT like some random cleaning company, It should be something UNIQUE). Of course by this flyers Marigold Cleaning Service should increase profits. If you will have any draft or any questions please contact me at any time on email: h.walters@mailbox-example.com or by phone: 07700900417
Best Regards
Hilda Walters
Marigold Cleaning Service LTD

```html
<!DOCTYPE html>
<html lang="en">
<head>
<meta charset="utf-8">
<title>Marigold Cleaning Service LTD – Flyer</title>
<link rel="stylesheet" href="https://fonts.googleapis.com/css2?family=Arimo:wght@400;700&family=Tinos:wght@400&display=swap">
<style>
  :root {
    --paper: #ffffff;
    --navy: #0a4f9e;
    --sky: #00c6f5;
    --ink: #0f2a44;
    --contact-ink: #23318c;
    --glow: rgba(190, 235, 255, 0.95);
  }
  html, body {
    margin: 0;
    padding: 0;
    overflow: hidden;
    background: var(--paper);
  }
  .flyer {
    position: relative;
    width: 1200px;
    height: 857px;
    overflow: hidden;
    background: var(--paper);
    font-family: "Arimo", Arial, sans-serif;
  }
  .flyer-shapes {
    position: absolute;
    inset: 0;
  }
  .offer-figure {
    position: absolute;
    left: 183px;
    top: 30px;
    margin: 0;
    font-family: "Arimo", Arial, sans-serif;
    font-weight: 400;
    font-size: 168px;
    line-height: 1;
    color: var(--paper);
    text-shadow: 0 0 18px var(--glow), 0 0 32px var(--glow);
  }
  .offer-note {
    position: absolute;
    left: 236px;
    top: 178px;
    width: 260px;
    margin: 0;
    text-align: center;
    font-family: "Tinos", "Times New Roman", serif;
    font-size: 30px;
    line-height: 32px;
    color: var(--paper);
    text-shadow: 0 0 10px var(--glow), 0 0 18px var(--glow);
  }
  .brand-name {
    position: absolute;
    left: 616px;
    top: 222px;
    margin: 0;
    font-family: "Arimo", Arial, sans-serif;
    font-weight: 400;
    font-size: 82px;
    line-height: 1;
    color: var(--ink);
  }
  .brand-sub {
    position: absolute;
    left: 540px;
    top: 342px;
    margin: 0;
    font-family: "Arimo", Arial, sans-serif;
    font-weight: 400;
    font-size: 57px;
    line-height: 1;
    color: var(--ink);
  }
  .contact-list {
    position: absolute;
    left: 32px;
    top: 444px;
    margin: 0;
    padding: 0;
    list-style: none;
    font-family: "Arimo", Arial, sans-serif;
    font-weight: 700;
    font-size: 17px;
    line-height: 21px;
    letter-spacing: -0.3px;
    color: var(--contact-ink);
  }
  .contact-list .contact-web {
    padding-left: 6px;
  }
  .slogan {
    position: absolute;
    left: 451px;
    top: 660px;
    margin: 0;
    font-family: "Tinos", "Times New Roman", serif;
    font-size: 44px;
    line-height: 1;
    color: var(--paper);
    letter-spacing: 0.5px;
    text-shadow: 0 0 10px var(--glow), 0 0 20px var(--glow);
    white-space: nowrap;
  }
</style>
</head>
<body>
<main class="flyer">
  <svg class="flyer-shapes" width="1200" height="857" viewBox="0 0 1200 857" xmlns="http://www.w3.org/2000/svg">
    <defs>
      <linearGradient id="swoosh-tones" x1="0" y1="0" x2="1" y2="0">
        <stop offset="0" stop-color="#b9d98a"/>
        <stop offset="0.2" stop-color="#f3e3a0"/>
        <stop offset="0.4" stop-color="#f2a27c"/>
        <stop offset="0.6" stop-color="#ee8fb0"/>
        <stop offset="0.8" stop-color="#a786c4"/>
        <stop offset="1" stop-color="#7fbde6"/>
      </linearGradient>
    </defs>
    <rect class="navy-field" x="0" y="24" width="1200" height="831" fill="var(--navy)"/>
    <polygon class="sky-wedge" points="0,24 518,494 0,855" fill="var(--sky)"/>
    <rect class="brand-panel" x="510" y="26" width="705" height="465" rx="42" fill="var(--paper)"/>
    <rect class="brand-swoosh" x="527" y="118" width="650" height="84" rx="30"
          fill="url(#swoosh-tones)" opacity="0.85"
          role="img" aria-label="Company logo artwork: a pastel rainbow swoosh ending in a leaping figure"/>
  </svg>

  <p class="offer-figure">5%</p>
  <p class="offer-note">discount for<br>new customers</p>

  <h1 class="brand-name">Marigold</h1>
  <p class="brand-sub">Cleaning Service LTD</p>

  <ul class="contact-list">
    <li class="contact-web">www.marigold-clean.example.co.uk</li>
    <li>Email address: marigoldservice@mailbox-example.com</li>
    <li>Mobile phone no: 07700900417</li>
    <li>Home no: 01632960582 .</li>
  </ul>

  <p class="slogan">“You Deserve Marigold Cleaners"</p>
</main>
</body>
</html>
```